Corporate brochure for a multinational construction company

Designing the cover pages and inside pages layout for a construction company which has operations in GCC, India etc. It has to be a very classy design. you can visit our website www.belvorant.com for more details on the company. Specific information required for the brochure design will be uploaded as needed.

Please note
1. Though the brochure will be around 80 pages, we need design of only the following
a. Cover page
b. CEOs message page
c. Introduction to sectors (Civil, Electrical, Mechanical, Infra)
d. Pages showing engineering expertise
e. Pages showing Project highlights (buildings etc)
f. Gallery pages (2 to 4 images in each page showing completed projects with a small text)
g. Key personnel (images and positions of key staff)

So design has to be done for a maximum of 7 to 10 pages. rest will be repetition.
Please use stock images with the above tip and send your designs.
g.
Updates

Project Deadline Extended
Reason: Not happy with the designs provided till now. Request all designers to once again look at the brief which is updated and submit maximum revisions. The pay is committed so we will select the best in any case. wish you all the best.

Target Market(s)

International - Current operations in the GCC, India, Srilanka

Industry/Entity Type

Construction Company

Font styles to use
Serif
Sans Serif

Requirements
Must have
• 1. A great front cover design - this may run to the back cover also
• 2. Inside page layout - to have a common theme but different styling as required
• 3. More of images and less of text - can use full page, half page or quarter page images.
• 4. Different styling and sizes for fonts for better effect.
Nice to have
• 1. A4 landscape is what we have in mind. The size can be slightly reduced so that the 80 page brochure can fit into an A4 envelope

```html
<!DOCTYPE html>
<html lang="en">
<head>
<meta charset="utf-8">
<title>Belvorant – CEO Message Spread</title>
<link href="https://fonts.googleapis.com/css2?family=Open+Sans:ital,wght@0,300;0,400;0,700;1,400&display=swap" rel="stylesheet">
<style>
  :root {
    --backdrop: #e4e4e4;
    --paper: #ffffff;
    --paper-shade: #f1f1f1;
    --brand-green: #3f6b52;
    --brand-green-deep: #2f5a43;
    --brand-green-soft: #5e8a6c;
    --heading-green: #4c7a5c;
    --quote-green: #2f5e44;
    --accent-gold: #a08a3c;
    --accent-gold-line: #c9a94a;
    --body-ink: #2b2b2b;
  }
  * { box-sizing: border-box; margin: 0; padding: 0; }
  html, body { width: 1200px; height: 880px; overflow: hidden; }
  body {
    background: var(--backdrop);
    font-family: "Open Sans", sans-serif;
    color: var(--body-ink);
  }
  .spread {
    position: absolute;
    left: 30px; top: 170px;
    width: 1140px; height: 540px;
    display: flex;
    box-shadow: 0 18px 40px rgba(0,0,0,0.18);
  }
  .page { position: relative; width: 570px; height: 540px; background: var(--paper); overflow: hidden; }
  .page--left { display: flex; }
  .page--right { background: linear-gradient(90deg, var(--paper-shade) 0, var(--paper) 40px); }

  .title-panel {
    position: relative;
    width: 240px; height: 100%;
    background: linear-gradient(160deg, var(--brand-green-soft) 0%, var(--brand-green) 45%, var(--brand-green-deep) 100%);
  }
  .title-panel__photo { position: absolute; inset: 0; width: 100%; height: 100%; }
  .title-panel__heading {
    position: absolute; left: 52px; top: 205px;
    color: #fff; line-height: 1.1;
  }
  .title-panel__heading .strong { display: block; font-weight: 700; font-size: 21px; letter-spacing: 1px; }
  .title-panel__heading .light { display: block; font-weight: 300; font-size: 21px; letter-spacing: 1px; }
  .title-panel__rule {
    position: absolute; left: 52px; top: 258px;
    width: 188px; height: 1px; background: var(--accent-gold-line);
  }

  .message { flex: 1; padding: 34px 30px 20px 30px; }
  .message__heading {
    font-weight: 300; font-size: 13px; color: var(--heading-green);
    text-transform: uppercase; letter-spacing: 0.3px; margin-bottom: 12px;
  }
  .message p {
    font-size: 9.4px; line-height: 1.38; text-align: justify; margin-bottom: 10px;
  }
  .signature { font-size: 9.4px; font-weight: 700; line-height: 1.3; margin-top: 6px; }

  .hero {
    position: absolute; top: 0; left: 0; width: 570px; height: 220px; display: flex;
  }
  .hero__band { width: 24px; height: 100%; background: var(--accent-gold); }
  .hero__photo { flex: 1; height: 100%; }

  .portrait { position: absolute; left: 28px; top: 250px; width: 128px; height: 148px; }
  .quotes { position: absolute; left: 180px; top: 258px; width: 362px; }
  .quotes p {
    font-style: italic; font-size: 11px; line-height: 1.35; color: var(--quote-green);
    text-align: justify; margin-bottom: 14px;
  }
</style>
</head>
<body>
  <main class="spread">
    <section class="page page--left">
      <div class="title-panel">
        <svg class="title-panel__photo" role="img" aria-label="Green-tinted photograph of the company headquarters entrance with signage and greenery" viewBox="0 0 240 540" preserveAspectRatio="none">
          <rect width="240" height="540" fill="url(#panelTone)"/>
          <defs>
            <linearGradient id="panelTone" x1="0" y1="0" x2="1" y2="1">
              <stop offset="0" stop-color="#6d9479"/>
              <stop offset="0.5" stop-color="#4a775b"/>
              <stop offset="1" stop-color="#335f47"/>
            </linearGradient>
          </defs>
        </svg>
        <h1 class="title-panel__heading"><span class="strong">CEO</span><span class="light">MESSAGE</span></h1>
        <div class="title-panel__rule"></div>
      </div>
      <article class="message">
        <h2 class="message__heading">A Partnership Construct</h2>
        <p>From humble beginnings with consistent hard work, dedication and an eye for the future, Belvorant has been transformed into an award-winning, nationally recognized integrated engineering construction services firm. We pride ourselves on being a home-grown Omani firm but imbued with an ambition to eventually expand across the Middle East and the Indian Subcontinent.</p>
        <p>Our forte lies in delivering end-to-end solutions that respond to our customers' needs. Belvorant's integrated, cross-discipline approach ensures that our clients benefit not only from the services we provide to them, but also from the full range of our expertise. We bring to the table unmatched competencies in civil, mechanical and electricity engineering, backed by top-flight EPC and project management support.</p>
        <p>But, more than our extensive portfolio, what truly sets us apart from our competition is our people. Their dedication to providing world-class service to our clients, capacity for innovation and problem solving, and unwavering commitment to improving the construction industry we serve, not only make Belvorant a great place to work, but a company with which our clients want to work.</p>
        <p>As one of Oman's most established contractors, Belvorant's vision is rooted in a desire to partner alongside the government of His Majesty the Sultan in developing the nation's infrastructure and driving its modernization. Central to this vision is also our commitment to providing rewarding careers to young Omani men and women drawn especially from the communities and locations in which we operate. By working hand in hand with the government authorities, our goal is to help crystallize the developmental aspirations of Oman for the ultimate benefit of its people.</p>
        <div class="signature">Dr. Martin Kessler<br>CEO</div>
      </article>
    </section>

    <section class="page page--right">
      <div class="hero">
        <div class="hero__band"></div>
        <svg class="hero__photo" role="img" aria-label="Aerial photograph of a large modern office building with vertical fins and a glass dome in a desert city" viewBox="0 0 546 220" preserveAspectRatio="none">
          <defs>
            <linearGradient id="heroTone" x1="0" y1="0" x2="0" y2="1">
              <stop offset="0" stop-color="#c9c3b4"/>
              <stop offset="0.35" stop-color="#b6a58a"/>
              <stop offset="0.7" stop-color="#7f8a72"/>
              <stop offset="1" stop-color="#8c8a80"/>
            </linearGradient>
          </defs>
          <rect width="546" height="220" fill="url(#heroTone)"/>
        </svg>
      </div>
      <svg class="portrait" role="img" aria-label="Portrait photograph of the CEO in a suit against a yellow backdrop" viewBox="0 0 128 148" preserveAspectRatio="none">
        <defs>
          <linearGradient id="portraitTone" x1="0" y1="0" x2="0" y2="1">
            <stop offset="0" stop-color="#d9a92a"/>
            <stop offset="0.6" stop-color="#8a6a3a"/>
            <stop offset="1" stop-color="#3a3f4e"/>
          </linearGradient>
        </defs>
        <rect width="128" height="148" fill="url(#portraitTone)"/>
      </svg>
      <div class="quotes">
        <p>"We pride ourselves on being a home-grown Omani firm but imbued with an ambition to eventually expand across the Middle East and the Indian Subcontinent."</p>
        <p>"Our forte lies in delivering end-to-end solutions that respond to our customers' needs. Belvorant's integrated, cross-discipline approach ensures that our clients benefit not only from the services we provide to them, but also from the full range of our expertise."</p>
        <p>"Belvorant's vision is rooted in a desire to partner alongside the government of His Majesty the Sultan in developing the nation's infrastructure and driving its modernization."</p>
      </div>
    </section>
  </main>
</body>
</html>
```